Brightstone Roofing Business Card

This is my current business card. But I’d like to make some changes. Somewhere on the card I’d like to list some of the services we offer. Maybe on the back? But I’d still like to keep the red. White and black modern look.

-residential & commercial roofing
-Roof Repairs & Maintenance
-Storm Damage & Insurance Claims specialist
-Christmas Lights and permanent Christmas lights
Fencing. Windows. Gutters. Siding. Sheetrock, painting.

```html
<!DOCTYPE html>
<html lang="en">
<head>
<meta charset="utf-8">
<title>Brightstone Roofing Co. – Business Card</title>
<link href="https://fonts.googleapis.com/css2?family=Arimo:wght@400;700&family=Audiowide&display=swap" rel="stylesheet">
<style>
  :root {
    --red: #e0202a;
    --black: #0a0a0a;
    --white: #ffffff;
    --paper: #f4f4f4;
    --grey: #6b6b6b;
    --faint: #e2e2e2;
    --stage: #d9d6d1;
  }
  * { box-sizing: border-box; margin: 0; padding: 0; }
  html, body { width: 1200px; height: 900px; overflow: hidden; }
  body {
    background: var(--stage);
    font-family: "Arimo", Arial, sans-serif;
    position: relative;
  }
  .card {
    position: absolute;
    left: 270px;
    width: 660px;
    height: 380px;
    border-radius: 34px;
    overflow: hidden;
    box-shadow: 0 10px 24px rgba(0,0,0,0.25);
  }
  .card--back { top: 50px; background: var(--black); color: var(--white); }
  .card--front { top: 470px; background: linear-gradient(135deg, var(--white), var(--paper)); color: var(--black); }

  .brand {
    position: absolute;
    right: 44px;
    top: 40px;
    display: flex;
    flex-direction: column;
    align-items: center;
    gap: 14px;
  }
  .brand__mark {
    width: 96px; height: 96px;
    border-radius: 50%;
    background: var(--red);
  }
  .brand__name {
    font-weight: 700;
    font-size: 26px;
    line-height: 1.1;
    letter-spacing: 2px;
    text-align: center;
    color: var(--red);
    text-transform: uppercase;
  }

  .services {
    position: absolute;
    left: 40px;
    bottom: 40px;
    font-size: 14.5px;
    line-height: 1.6;
  }
  .services__title {
    color: var(--red);
    font-size: 19px;
    font-weight: 400;
    letter-spacing: 0.5px;
    margin-bottom: 2px;
  }

  .watermark {
    position: absolute;
    left: -40px;
    top: 60px;
    width: 280px;
    height: 280px;
    border-radius: 50%;
    background: var(--faint);
  }

  .rule {
    position: absolute;
    height: 1px;
    background: var(--grey);
  }
  .rule--top { left: 330px; right: 34px; top: 250px; }
  .rule--bottom { left: 34px; right: 330px; top: 320px; }

  .person {
    position: absolute;
    left: 40px;
    top: 278px;
    display: flex;
    align-items: baseline;
    gap: 8px;
  }
  .person__name {
    font-family: "Audiowide", "Arimo", sans-serif;
    color: var(--red);
    font-size: 24px;
    letter-spacing: 1px;
  }
  .person__sep { color: var(--red); font-size: 22px; }
  .person__role { font-size: 17px; letter-spacing: 0.5px; }

  .contact {
    position: absolute;
    left: 40px;
    right: 34px;
    top: 334px;
    display: flex;
    align-items: center;
    gap: 8px;
    font-size: 14px;
    color: #222;
    white-space: nowrap;
  }
  .contact__item { display: flex; align-items: center; gap: 6px; }
  .contact__icon { width: 15px; height: 15px; flex: none; }
  .contact__sep { color: var(--grey); }
</style>
</head>
<body>

<section class="card card--back" aria-label="Card back">
  <div class="brand">
    <span class="brand__mark"></span>
    <span class="brand__name">Brightstone<br>Roofing Co.</span>
  </div>
  <div class="services">
    <h2 class="services__title">SERVICES</h2>
    <p>Residential &amp; Commercial Roofing / Roof Repairs &amp; Maintenance</p>
    <p>Storm Damage &amp; Insurance Claims Specialist</p>
    <p>Christmas Lights And Permanent Christmas Lights / Fencing. Windows</p>
    <p>Gutters. Siding. Sheetrock, painting.</p>
  </div>
</section>

<section class="card card--front" aria-label="Card front">
  <div class="watermark" role="img" aria-label="Faint brand emblem area"></div>
  <div class="brand">
    <span class="brand__mark"></span>
    <span class="brand__name">Brightstone<br>Roofing Co.</span>
  </div>
  <div class="rule rule--top"></div>
  <div class="person">
    <span class="person__name">DALE MORGAN</span>
    <span class="person__sep">|</span>
    <span class="person__role">OWNER</span>
  </div>
  <div class="rule rule--bottom"></div>
  <div class="contact">
    <span class="contact__item">
      <svg class="contact__icon" viewBox="0 0 24 24" aria-hidden="true"><path fill="#e0202a" d="M6.6 10.8a15.1 15.1 0 0 0 6.6 6.6l2.2-2.2a1 1 0 0 1 1-.25 11.4 11.4 0 0 0 3.6.57 1 1 0 0 1 1 1V20a1 1 0 0 1-1 1A17 17 0 0 1 3 4a1 1 0 0 1 1-1h3.5a1 1 0 0 1 1 1c0 1.25.2 2.45.57 3.6a1 1 0 0 1-.25 1z"/></svg>
      555-014-2290
    </span>
    <span class="contact__sep">|</span>
    <span class="contact__item">
      <svg class="contact__icon" viewBox="0 0 24 24" aria-hidden="true"><rect x="2" y="5" width="20" height="14" rx="1" fill="#e0202a"/><path d="M2 6l10 7 10-7" fill="none" stroke="#fff" stroke-width="1.6"/></svg>
      Dale@brightstoneroofing.co
    </span>
    <span class="contact__sep">|</span>
    <span class="contact__item">
      <svg class="contact__icon" viewBox="0 0 24 24" aria-hidden="true"><g fill="none" stroke="#e0202a" stroke-width="1.8"><circle cx="12" cy="12" r="9.5"/><ellipse cx="12" cy="12" rx="4" ry="9.5"/><path d="M2.5 12h19M4 7h16M4 17h16"/></g></svg>
      www.brightstoneroofing.co
    </span>
  </div>
</section>

</body>
</html>
```